Cobalt-Ridge Playbook Book Cover

Cobalt-Ridge Playbook is a Self-Assessment and Feasibility Workbook for Small Business Start-ups. It is for nascent entrepreneurs, anyone thinking about starting a business. The book is intended to be fun, non-threatening, easy, creative, inspirational, and planet friendly. It is for adults of all cultural and ethnic backgrounds. The book is 8.5" x 11" and we will need covers designed for both a paperback and an ebook.
Target Market(s)
Adult entrepreneurs. Anyone who hopes to start a small business. Targeting small business and micro-business start-ups, home-based, English-speaking audience.
Requirements
Must have
- Must be appropriate for all cultures and ethnic backgrounds. Must be fun, non-threatening, easy, creative, inspirational, and planet friendly.
Nice to have
- Book is a confidence-building adventure. Intended to remove the fear and stress from starting a small business.
Should not have
- Designs must be guaranteed to be free of third party copyright, such as Lumora, etc.

```html
<!DOCTYPE html>
<html lang="en">
<head>
<meta charset="utf-8">
<title>Cobalt-Ridge Playbook — Book Cover</title>
<link rel="stylesheet" href="https://fonts.googleapis.com/css2?family=Bebas+Neue&family=Oswald:wght@400&display=swap">
<style>
  :root {
    --sky-top: #16a2cd;
    --sky-mid: #2bdfe3;
    --sky-bottom: #1bb4d8;
    --title-white: #ffffff;
    --title-yellow: #fbef3a;
    --art-pink: #c7235f;
    --art-green: #6dbb2a;
  }
  html, body {
    margin: 0;
    padding: 0;
    overflow: hidden;
    background: var(--sky-mid);
  }
  .cover {
    position: relative;
    width: 927px;
    height: 1200px;
    overflow: hidden;
    background: linear-gradient(180deg, var(--sky-top) 0%, var(--sky-mid) 55%, var(--sky-bottom) 100%);
  }
  .cover-title {
    position: absolute;
    left: 0;
    top: 0;
    width: 927px;
    height: 470px;
  }
  .cover-title text {
    font-family: "Bebas Neue", "Oswald", sans-serif;
    font-size: 246px;
  }
  .title-line-top { fill: var(--title-white); }
  .title-line-bottom { fill: var(--title-yellow); }
  .cover-art {
    position: absolute;
    left: 152px;
    top: 476px;
    width: 528px;
    height: 576px;
    border-radius: 24px;
    background: linear-gradient(200deg, rgba(199, 35, 95, 0.55) 0%, rgba(199, 35, 95, 0.25) 55%, rgba(109, 187, 42, 0.45) 100%);
  }
  .cover-author {
    position: absolute;
    left: 0;
    top: 1096px;
    width: 927px;
    margin: 0;
    padding-left: 50px;
    box-sizing: border-box;
    text-align: center;
    font-family: "Oswald", sans-serif;
    font-weight: 400;
    font-size: 58px;
    line-height: 1;
    letter-spacing: 0.22em;
    color: var(--title-white);
  }
</style>
</head>
<body>
  <main class="cover">
    <svg class="cover-title" viewBox="0 0 927 470" role="heading" aria-level="1" aria-label="Cobalt-Ridge Playbook">
      <text class="title-line-top" x="56" y="232" textLength="816" lengthAdjust="spacingAndGlyphs">COBALT-RIDGE</text>
      <text class="title-line-bottom" x="56" y="448" textLength="816" lengthAdjust="spacingAndGlyphs">PLAYBOOK</text>
    </svg>
    <div class="cover-art" role="img" aria-label="Illustration: a pink watering can pouring water drops onto a small green sprout growing from a mound of soil"></div>
    <p class="cover-author">AUTHOR´S NAME</p>
  </main>
</body>
</html>
```